Business card and company stationary - Corvane Cleaning Ltd

1. Who are we and who are our customers?

o We are a relatively new cleaning company, established December 2008. We are a small company. We have 24 staff and we offer domestic and commercial cleaning services.
o We both (me and my wife) have been working for many years in the cleaning industry. We worked for some of the biggest and best cleaning companies in UK. We’ve been operatives, supervisors and managers.
o Inevitably after so many years of working for someone else, we decided to start our own business.
o Our domestic customers are middle class families and busy professionals. We’ve got some commercial customers, mainly offices.
o We are growing steadily.

2. What do we do? What are our services?

o Cleaning. We’ve got range of services - not to many but still can be daunting and confusing for some.
o Generally we’ve got domestic and commercial clients. The approach to the domestic cleaning customers is different to the commercial. In the way we want to say that it is cleaning that we do, but we acknowledge the environment and we appreciate the personal circumstances and requirements that are present. We do care, we listen and we try to work out the best possible way to complete our work.
o Mainly we get our work through referrals

3. What do we want with our stationery ?

o To place and maintain our message and reach out to people and organisations
o We want to advertise, communicate and sale.
o We are going to sell services.
o Increase membership, loyalty and support.

We are after business card design, headed letter and compliment slip.
We would like the headed letter to be created in formats suitable for :
- printing format
- also for use in our daily correspondence via e mail with clients and staff in a easy to edit and write format

The website we have is still under contraction and the domain is corvanecleaning.example

Target Market(s)

Families, individuals, businesses.

Industry/Entity Type

Cleaning Service

Contact Information for Business Card

FRONT :
Company Name - Corvane Cleaning Ltd
Company address - 41 Pelbury Rd, Pelbury, Essex, RM14 7QT
Name - Mrs. Teodora Vasilkova - Tedi
Title - Managing Director
Company phone - 020 8837 2591
E mail - tedi.vasilkova@corvanecleaning.example

BACK :

Company website - corvanecleaning.example
E mail - enquiries@corvanecleaning.example

Font styles to use
Serif

Requirements
Must have
• The above items and company logo...maybe at the back. But I'm free for any suggestions.

```html
<!DOCTYPE html>
<html lang="en">
<head>
<meta charset="utf-8">
<title>Corvane Cleaning Ltd – Business Card</title>
<link rel="stylesheet" href="https://fonts.googleapis.com/css2?family=Lora:wght@400&display=swap">
<style>
  :root {
    --brand-blue: #37c5f3;
    --brand-blue-soft: rgba(255, 255, 255, 0.16);
    --ink-grey: #6a6a6a;
    --paper: #ffffff;
    --backdrop: #ffffff;
  }
  * { margin: 0; padding: 0; box-sizing: border-box; }
  html, body {
    width: 1041px;
    height: 1200px;
    overflow: hidden;
    background: var(--backdrop);
    font-family: "Lora", Georgia, serif;
  }
  .canvas { position: relative; width: 1041px; height: 1200px; }

  .card {
    position: absolute;
    left: 169px;
    width: 685px;
    height: 385px;
    overflow: hidden;
  }

  /* Front */
  .card--front { top: 159px; background: var(--paper); outline: 1px solid #eeeeee; }
  .front__mark {
    position: absolute;
    left: 245px;
    top: 35px;
    width: 194px;
    height: 194px;
    border-radius: 50%;
    background: var(--brand-blue);
  }
  .front__name {
    position: absolute;
    left: 0;
    right: 0;
    top: 264px;
    text-align: center;
    color: var(--ink-grey);
    font-size: 32px;
    letter-spacing: 5px;
    text-transform: uppercase;
  }

  /* Back */
  .card--back { top: 650px; background: var(--brand-blue); }
  .back__strip {
    position: absolute;
    left: 38px;
    top: 0;
    width: 95px;
    height: 366px;
    background: var(--paper);
  }
  .back__mark {
    position: absolute;
    left: 11px;
    top: 286px;
    width: 70px;
    height: 70px;
    border-radius: 50%;
    background: var(--brand-blue);
  }
  .back__decor {
    position: absolute;
    left: 494px;
    top: 289px;
    width: 176px;
    height: 176px;
    border-radius: 50%;
    background: var(--brand-blue-soft);
  }
  .back__details {
    position: absolute;
    left: 153px;
    top: 64px;
    color: var(--paper);
  }
  .person__name { font-size: 36px; line-height: 1; font-weight: 400; }
  .person__title { font-size: 21px; margin-top: 10px; }
  .contact { list-style: none; font-size: 17px; line-height: 24px; }
  .contact--direct { margin-top: 18px; }
  .contact--online { margin-top: 22px; }
  .contact--post { margin-top: 22px; }
</style>
</head>
<body>
<main class="canvas">
  <section class="card card--front" aria-label="Business card front">
    <div class="front__mark"></div>
    <p class="front__name">Corvane Cleaning Ltd</p>
  </section>

  <section class="card card--back" aria-label="Business card back">
    <div class="back__decor"></div>
    <div class="back__strip">
      <div class="back__mark"></div>
    </div>
    <div class="back__details">
      <h1 class="person__name">Teodora Vasilkova</h1>
      <p class="person__title">Managing Director</p>
      <ul class="contact contact--direct">
        <li>Phone: 020 8837 2591</li>
        <li>Email: tedi.vasilkova@corvanecleaning.example</li>
      </ul>
      <ul class="contact contact--online">
        <li>Enquiries: enquiries@corvanecleaning.example</li>
        <li>Web: corvanecleaning.example</li>
      </ul>
      <ul class="contact contact--post">
        <li>Address: 41 Pelbury Rd, Pelbury, Essex, RM14 7QT</li>
      </ul>
    </div>
  </section>
</main>
</body>
</html>
```